Brell Harbor Company Business Cards

Front and Back Business Card - logo and text setup - cool design. I need workable photoshop or illustrator files so I can setup each employee card with design that is created
Updates

Hi everyone, thank you for the great entries. Please no more white and blue cards - there are so many already - black and silver only now please. thanks!

Target Market(s)

Construction Industry - Facility Managers

Industry/Entity Type

Construction

Contact Information for Business Card

I really like contemporary simplistic looks - clean neat....not opposed to seeing some black backrounds

Requirements
Must have
• Logo/website address with design on front only - www.brellharbor-example.com (logo attached)
• Back:
• Name/Title/Company Address/Phone/email address
Nice to have
• Cool design
Should not have
• Nothing gimmicky like Fire or Water - since we are a Fire Protection company - it has all been done

```html
<!DOCTYPE html>
<html lang="en">
<head>
<meta charset="utf-8">
<title>Brell Harbor Company — Business Cards</title>
<link href="https://fonts.googleapis.com/css2?family=Lato:wght@400;900&display=swap" rel="stylesheet">
<style>
  :root {
    --backdrop: #1c1c1e;
    --card-red: #ef4b37;
    --card-white: #ffffff;
    --logo-pale: #fbd3ca;
    --navy: #27386b;
    --accent: #ee4a30;
    --ink: #4a4a4a;
    --rule: #d6d6d6;
  }
  * { margin: 0; padding: 0; box-sizing: border-box; }
  html, body {
    width: 1200px; height: 900px; overflow: hidden;
    background: var(--backdrop);
    font-family: "Lato", Arial, sans-serif;
  }
  .stage {
    width: 1200px; height: 900px;
    display: flex; align-items: center; justify-content: center; gap: 48px;
  }
  .card {
    position: relative;
    width: 520px; height: 300px;
    border-radius: 22px;
    box-shadow: 0 18px 40px rgba(0,0,0,.55);
    overflow: hidden;
  }
  /* Front */
  .card--front { background: var(--card-red); }
  .card--front .wordmark {
    position: absolute; left: 0; right: 0; top: 112px;
    text-align: center;
    font-weight: 900; font-size: 46px; letter-spacing: -1px;
    color: var(--logo-pale);
  }
  .card--front .site {
    position: absolute; left: 0; right: 0; bottom: 40px;
    text-align: center;
    font-size: 13px; color: #fff;
  }
  /* Back */
  .card--back { background: var(--card-white); }
  .card--back .wordmark {
    position: absolute; right: 36px; top: 52px;
    display: flex; align-items: center; gap: 10px;
    font-weight: 900; font-size: 36px; letter-spacing: -0.5px;
    color: var(--navy);
  }
  .wordmark-square {
    width: 14px; height: 14px; background: var(--navy);
  }
  .card--back .logo-rule {
    position: absolute; right: 36px; top: 112px;
    width: 240px; height: 1px; background: var(--rule);
  }
  .card--back .address {
    position: absolute; right: 36px; top: 128px;
    text-align: right;
    font-size: 14px; line-height: 1.35; color: var(--ink);
  }
  .card--back .person {
    position: absolute; left: 34px; top: 176px; right: 36px;
  }
  .person-name {
    display: flex; align-items: center; gap: 12px;
    font-size: 17px; letter-spacing: .5px; color: var(--accent);
    text-transform: uppercase;
  }
  .person-name::after {
    content: ""; flex: 1; height: 1px; background: var(--rule);
  }
  .person-title { font-size: 14px; color: var(--ink); margin-top: 1px; }
  .contact-list { list-style: none; margin-top: 10px; }
  .contact-list li {
    display: flex; align-items: center; gap: 8px;
    font-size: 14px; line-height: 1.45; color: var(--ink);
  }
  .contact-list svg { width: 12px; height: 12px; flex: none; }
</style>
</head>
<body>
<main class="stage">

  <section class="card card--front" aria-label="Business card front">
    <div class="wordmark">Brell Harbor</div>
    <div class="site">www.brellharbor-example.com</div>
  </section>

  <section class="card card--back" aria-label="Business card back">
    <div class="wordmark"><span class="wordmark-square"></span>Brell Harbor</div>
    <div class="logo-rule"></div>
    <address class="address">
      88 Quayside Row<br>
      Harborland, 40217
    </address>

    <div class="person">
      <div class="person-name">Marten Oyelaran</div>
      <div class="person-title">Managing Director</div>
      <ul class="contact-list">
        <li>
          <svg viewBox="0 0 12 12" aria-hidden="true"><path fill="#ee4a30" d="M2.2 1h2l.9 2.4-1.2.9a6.5 6.5 0 0 0 3.8 3.8l.9-1.2 2.4.9v2c0 .7-.6 1.2-1.3 1.2C5 10.7 1.3 7 1 2.3 1 1.6 1.5 1 2.2 1z"/></svg>
          044-555 019 230
        </li>
        <li>
          <svg viewBox="0 0 12 12" aria-hidden="true"><rect x="0.5" y="2" width="11" height="8" fill="#ee4a30"/><path d="M1 2.6l5 3.6 5-3.6" stroke="#fff" stroke-width="1" fill="none"/></svg>
          info@brellharbor-example.com
        </li>
        <li>
          <svg viewBox="0 0 12 12" aria-hidden="true"><circle cx="6" cy="6" r="5.5" fill="#ee4a30"/><ellipse cx="6" cy="6" rx="2.3" ry="5.2" stroke="#fff" stroke-width=".8" fill="none"/><path d="M.8 6h10.4" stroke="#fff" stroke-width=".8"/></svg>
          www.brellharbor-example.com
        </li>
      </ul>
    </div>
  </section>

</main>
</body>
</html>
```